Velbrin Redesign of Website

I require my webpage to look different but this is out with my current providers platform
I will benefit from designs that use my wording (this is extremely important). I appreciate there may be a lot of wording in some areas so i would be happy with "read more" in various places. The use of my face in photo is a must and my logo is also a must which can be found on m y website www.velbrinadhd.co.uk I do not want corporate feel, i would like a warm, authentic. personal and inviting feel.

```html
<!DOCTYPE html>
<html lang="en">
<head>
<meta charset="utf-8">
<title>The Story Behind Velbrin</title>
<link href="https://fonts.googleapis.com/css2?family=Josefin+Sans:wght@400;600&family=Inter:wght@400;500;600&family=Cormorant+Garamond:wght@500&display=swap" rel="stylesheet">
<style>
:root{
  --teal:#1a9f80;
  --teal-dark:#137a62;
  --teal-deep:#0f5c4a;
  --mint:#e4f4f0;
  --mint-card:#f2faf8;
  --badge-fill:#e2efeb;
  --ink:#222;
  --grey:#8a8a8a;
  --white:#fff;
}
*{box-sizing:border-box;margin:0;padding:0}
html,body{width:1200px;height:5089px;overflow:hidden;background:var(--white)}
body{font-family:"Inter",Arial,sans-serif;color:var(--ink);position:relative}
.abs{position:absolute}
.head{font-family:"Josefin Sans",Arial,sans-serif;text-transform:uppercase;font-weight:400;letter-spacing:1px}

/* hero */
.hero{left:0;top:0;width:1200px;height:532px;background:linear-gradient(100deg,#3d443f 0%,#4f5a52 45%,#6d6a60 100%)}
.hero-photo{left:640px;top:0;width:560px;height:532px;background:radial-gradient(ellipse at 60% 40%,#c89c84 0%,#9b7b68 35%,#55534d 75%)}
.menu{left:64px;top:48px;width:24px}
.menu span{display:block;height:3px;background:var(--white);margin-bottom:4px}
.brand{left:110px;top:40px;width:500px;text-align:center;color:var(--white)}
.brand-mark{width:64px;height:64px;border-radius:50%;background:var(--white);margin:0 auto 38px}
.brand-name{font-family:"Cormorant Garamond",serif;font-size:15px;letter-spacing:1px;text-transform:uppercase}
.brand-tag{font-size:10px;letter-spacing:6px;margin-top:8px;text-transform:uppercase}
.hero-title{left:110px;top:345px;width:490px;text-align:center;color:var(--white);font-size:46px;line-height:52px}
.hero-sub{left:110px;top:460px;width:490px;text-align:center;color:var(--white);font-size:15px}

/* intro */
.intro{left:0;top:532px;width:1200px;height:525px;background:linear-gradient(180deg,#1ea585,#17967a)}
.avatar{left:558px;top:608px;width:84px;height:84px;border-radius:50%;background:linear-gradient(135deg,#b08a76,#556);border:3px solid #d5efe8}
.intro-title{left:250px;top:716px;width:700px;text-align:center;color:var(--white);font-size:21px;line-height:34px}
.intro-text{left:220px;top:792px;width:760px;text-align:center;color:#e9f7f3;font-size:13.5px;line-height:26px}
.divider{left:510px;top:896px;width:180px;height:16px}
.intro-quote{left:270px;top:930px;width:660px;text-align:center;color:var(--white);font-size:14px;line-height:26px}

/* journey */
.sec-title{width:1200px;left:0;text-align:center;font-size:44px;color:var(--ink)}
.step{width:205px;text-align:center}
.step-ring{width:150px;height:150px;border-radius:50%;border:2px dashed #8fd1c0;margin:0 auto;padding:10px}
.step-ring .dot{width:100%;height:100%;border-radius:50%;background:var(--teal);display:flex;align-items:center;justify-content:center}
.step-lead{font-size:13px;font-weight:500;line-height:23px;margin-top:42px;color:#333}
.step-body{font-size:11.5px;color:var(--grey);line-height:20px;margin-top:12px}

/* why */
.why{left:0;top:1815px;width:1200px;height:770px;background:var(--mint)}
.why-card{left:112px;top:1975px;width:466px;height:535px;background:var(--white);border:2px solid #9ad7c6;border-radius:40px;padding:42px 44px}
.why-item h4{color:var(--teal);font-size:14.5px;font-weight:600;line-height:26px;padding-left:36px;position:relative}
.why-item h4::before{content:"";position:absolute;left:0;top:6px;width:13px;height:13px;border-radius:50%;background:var(--teal)}
.why-item p{color:#777;font-size:13.5px;line-height:26px;margin:16px 0 30px;text-align:justify}
.why-photo{left:620px;top:1975px;width:468px;height:535px;border-radius:40px;background:linear-gradient(180deg,#f2c273 0%,#d38a3c 45%,#5b4430 80%,#2e2520 100%)}

/* path */
.path-title{left:113px;top:2672px;font-size:44px}
.btn{background:var(--teal);color:var(--white);border-radius:26px;font-size:15px;font-weight:600;text-align:center}
.path-btn{left:937px;top:2672px;width:148px;height:52px;line-height:52px}
.tile{width:226px;height:230px;background:var(--mint-card);border:1.5px solid #cdeae2;border-radius:22px;text-align:center;padding-top:42px}
.tile .ic{width:86px;height:86px;border-radius:50%;background:var(--teal);margin:0 auto 28px;display:flex;align-items:center;justify-content:center}
.tile p{font-size:14px;line-height:21px;color:#333;padding:0 16px}

/* approach */
.approach{left:0;top:3360px;width:1200px;height:593px;background:linear-gradient(180deg,#1a9a7c,#178f74)}
.approach-photo{left:112px;top:3445px;width:488px;height:423px;border-radius:70px 0 70px 0;background:linear-gradient(180deg,#7c9bb5 0%,#a9b6ba 40%,#6f7369 70%,#4c4a40 100%)}
.approach-title{left:665px;top:3496px;color:var(--white);font-size:44px;line-height:54px}
.approach-sub{left:665px;top:3615px;color:var(--white);font-size:17px}
.approach-list{left:685px;top:3664px;list-style:none;color:var(--white);font-size:15px}
.approach-list li{height:41px;display:flex;align-items:center}
.approach-list svg{margin-right:20px}

/* difference */
.diff-icon{left:540px;top:4065px;width:120px;height:120px;border-radius:50%;background:var(--teal);display:flex;align-items:center;justify-content:center}
.diff-title{left:200px;top:4225px;width:800px;text-align:center;font-size:40px;line-height:56px;color:var(--ink)}
.diff-text{left:225px;top:4392px;width:750px;text-align:center;color:var(--grey);font-size:19px;line-height:36px}
.badge{top:4550px;width:317px;height:212px;border:2px solid #bfe4d9;border-radius:26px;overflow:hidden;background:var(--white)}
.badge .shape{height:150px;display:flex;align-items:center;justify-content:center}
.badge .label{height:62px;background:var(--teal);color:var(--white);font-size:14px;font-weight:600;display:flex;align-items:center;justify-content:center;text-transform:uppercase;letter-spacing:.3px}

/* cta + footer */
.cta{left:0;top:4852px;width:1200px;height:188px;background:linear-gradient(180deg,#1a987b,#15876d)}
.cta-title{left:110px;top:4920px;color:var(--white);font-size:34px;line-height:46px}
.cta-btn{left:878px;top:4916px;width:207px;height:52px;line-height:52px;background:var(--white);color:var(--teal)}
.footer{left:0;top:5040px;width:1200px;height:49px;background:var(--teal-deep);color:var(--white);font-size:13px;text-align:center;line-height:49px}
</style>
</head>
<body>

<!-- hero -->
<section class="abs hero"></section>
<div class="abs hero-photo" role="img" aria-label="Smiling portrait of the Velbrin founder outdoors on a farm"></div>
<div class="abs menu"><span></span><span></span><span></span></div>
<div class="abs brand">
  <div class="brand-mark"></div>
  <div class="brand-name">Velbrin ADHD Coaching and Wellbeing</div>
  <div class="brand-tag">Empower your mind, transform your life</div>
</div>
<h1 class="abs head hero-title">The Story Behind Velbrin</h1>
<p class="abs hero-sub">Helping others began with understanding myself.</p>

<!-- intro -->
<section class="abs intro"></section>
<div class="abs avatar" role="img" aria-label="Small round portrait of the founder"></div>
<h2 class="abs head intro-title">My name is Lorna Baird Kerr.<br>Founder of Velbrin.</h2>
<p class="abs intro-text">I am an ADHD coach and wellbeing practitioner with lived experience of ADHD and autism. I combine professional expertise with real-life experience to offer compassionate, practical support that helps you better understand yourself, your brain and your wellbeing.</p>
<svg class="abs divider" viewBox="0 0 180 16"><line x1="0" y1="8" x2="78" y2="8" stroke="#cdeee5"/><line x1="102" y1="8" x2="180" y2="8" stroke="#cdeee5"/><path d="M90 14 L83 7 A3.5 3.5 0 0 1 90 4 A3.5 3.5 0 0 1 97 7 Z" fill="#fff"/></svg>
<p class="abs intro-quote">You don't need to have everything figured out before reaching out. We'll take things one step at a time, together.</p>

<!-- journey -->
<h2 class="abs head sec-title" style="top:1140px">My Journey</h2>
<div class="abs step" style="left:128px;top:1215px">
  <div class="step-ring"><div class="dot"><svg width="60" height="60" viewBox="0 0 60 60" fill="none" stroke="#fff" stroke-width="2.5"><path d="M30 10 C18 10 12 18 12 28 C12 40 20 48 30 48 C40 48 48 40 48 28 C48 18 42 10 30 10 Z"/><path d="M30 10 V48 M20 22 C24 24 24 30 20 32 M40 22 C36 24 36 30 40 32"/></svg></div></div>
  <p class="step-lead">My adult ADHD diagnosis came during a period of profound self-discovery following a mental health breakdown.</p>
  <p class="step-body">For many years, my ADHD went unrecognised and was treated only with antidepressants, which never addressed the underlying cause of my struggles. Learning about ADHD didn't cause my breakdown – it helped explain it.</p>
</div>
<div class="abs step" style="left:390px;top:1282px">
  <div class="step-ring"><div class="dot"><svg width="60" height="60" viewBox="0 0 60 60" fill="none" stroke="#fff" stroke-width="2.5"><circle cx="30" cy="30" r="20"/><circle cx="24" cy="26" r="6"/><circle cx="36" cy="34" r="6"/></svg></div></div>
  <p class="step-lead">As my understanding grew, I recognised I am also autistic – something that is common alongside ADHD.</p>
  <p class="step-body">Around 50–70% of autistic people also have ADHD, and many adults only recognise the second neurotype once the first has been identified. This combined experience is often called AuDHD. For me, it brought even greater clarity.</p>
</div>
<div class="abs step" style="left:640px;top:1215px">
  <div class="step-ring"><div class="dot"><svg width="60" height="60" viewBox="0 0 60 60" fill="none" stroke="#fff" stroke-width="2.5"><path d="M20 48 V38 C14 34 12 28 14 22 C17 12 30 8 40 14 C48 20 48 30 44 36 V48"/><circle cx="31" cy="25" r="6"/></svg></div></div>
  <p class="step-lead">These experiences strengthened my passion for helping neurodivergent individuals better understand their brains, develop self-compassion and find strategies that work.</p>
  <p class="step-body">I believe every brain deserves understanding, support and practical tools for wellbeing.</p>
</div>
<div class="abs step" style="left:878px;top:1282px">
  <div class="step-ring"><div class="dot"><svg width="60" height="60" viewBox="0 0 60 60" fill="none" stroke="#fff" stroke-width="2.5"><path d="M10 40 L30 46 L50 40 V20 L30 26 L10 20 Z M30 26 V46"/><circle cx="30" cy="14" r="5"/></svg></div></div>
  <p class="step-lead">This personal journey inspired me to deepen my professional knowledge and training.</p>
  <p class="step-body">I qualified as an Integrative Counsellor (HNC) and then as a Health &amp; Wellbeing Coach through Open Meadow Academy (nationally recognised), followed by specialist training in Autism, ADHD and Somatic Coaching.</p>
</div>

<!-- why -->
<section class="abs why"></section>
<h2 class="abs head sec-title" style="top:1885px">Why Velbrin Was Created</h2>
<div class="abs why-card">
  <div class="why-item"><h4>I wanted to offer the kind of support I wish I had when I was struggling.</h4><p>A safe, welcoming space where neurodivergent people feel seen, understood and supported to thrive in their own way.</p></div>
  <div class="why-item"><h4>I believe in practical, lasting support.</h4><p>I empower people with knowledge, strategies and tools they can continue using long after our work together has ended.</p></div>
  <div class="why-item"><h4>I understand the reality of neurodivergent family life.</h4><p>As a mother to three neurodivergent children, I have invaluable lived experience of advocacy, navigating systems &amp; creating a calmer home life.</p></div>
</div>
<div class="abs why-photo" role="img" aria-label="Woman standing on a mountain top at sunrise above the clouds"></div>

<!-- path -->
<h2 class="abs head path-title">My Path</h2>
<div class="abs btn path-btn">View More</div>
<div class="abs tile" style="left:113px;top:2760px"><div class="ic"><svg width="44" height="44" viewBox="0 0 44 44" fill="#fff"><path d="M6 22 L22 8 L38 22 V38 H6 Z"/></svg></div><p>Housing Officer</p></div>
<div class="abs tile" style="left:362px;top:2760px"><div class="ic"><svg width="44" height="44" viewBox="0 0 44 44" fill="#fff"><path d="M12 40 V30 C6 26 6 14 14 8 C22 2 36 6 38 18 L40 26 H36 V34 H28 V40 Z"/></svg></div><p>Mental Health Breakdown</p></div>
<div class="abs tile" style="left:611px;top:2760px"><div class="ic"><svg width="44" height="44" viewBox="0 0 44 44" fill="none" stroke="#fff" stroke-width="3"><path d="M22 4 V40 M4 22 H40 M9 9 L35 35 M35 9 L9 35"/></svg></div><p>ADHD Diagnosis</p></div>
<div class="abs tile" style="left:860px;top:2760px"><div class="ic"><svg width="44" height="44" viewBox="0 0 44 44" fill="#fff"><circle cx="22" cy="14" r="8"/><path d="M8 40 C8 28 36 28 36 40 Z"/></svg></div><p>Understanding Autism (AuDHD)</p></div>
<div class="abs tile" style="left:113px;top:3020px"><div class="ic"><svg width="44" height="44" viewBox="0 0 44 44" fill="#fff"><circle cx="22" cy="10" r="6"/><path d="M6 24 L22 30 L38 24 V38 L22 42 L6 38 Z"/></svg></div><p>Integrative Counselling Study</p></div>
<div class="abs tile" style="left:362px;top:3020px"><div class="ic"><svg width="44" height="44" viewBox="0 0 44 44" fill="#fff"><path d="M22 4 L38 10 V22 C38 32 30 38 22 41 C14 38 6 32 6 22 V10 Z"/><path d="M19 14 H25 V20 H31 V26 H25 V32 H19 V26 H13 V20 H19 Z" fill="#1a9f80"/></svg></div><p>Health &amp; Wellbeing Coach (nationally recognised)</p></div>
<div class="abs tile" style="left:611px;top:3020px"><div class="ic"><svg width="44" height="44" viewBox="0 0 44 44" fill="#fff"><path d="M22 40 L6 24 A9 9 0 0 1 22 10 A9 9 0 0 1 38 24 Z"/></svg></div><p>Specialist Training in Autism, ADHD &amp; Somatic Coaching</p></div>
<div class="abs tile" style="left:860px;top:3020px"><div class="ic"><svg width="44" height="44" viewBox="0 0 44 44" fill="#fff"><path d="M2 36 L16 14 L24 26 L30 18 L42 36 Z"/></svg></div><p>Velbrin Created</p></div>

<!-- approach -->
<section class="abs approach"></section>
<div class="abs approach-photo" role="img" aria-label="Stack of balanced stones on a rock beside a lake"></div>
<h2 class="abs head approach-title">The Velbrin<br>Approach</h2>
<p class="abs approach-sub">Everything I offer has Velbrin's heart &amp;purpose.</p>
<ul class="abs approach-list">
  <li><svg width="16" height="16" viewBox="0 0 16 16"><circle cx="8" cy="8" r="8" fill="#fff"/><path d="M4.5 8 L7 10.5 L11.5 5.5" stroke="#1a9a7c" stroke-width="2" fill="none"/></svg>Lived &amp; Tested</li>
  <li><svg width="16" height="16" viewBox="0 0 16 16"><circle cx="8" cy="8" r="8" fill="#fff"/><path d="M4.5 8 L7 10.5 L11.5 5.5" stroke="#1a9a7c" stroke-width="2" fill="none"/></svg>Individual, Not One-Size-Fits-All</li>
  <li><svg width="16" height="16" viewBox="0 0 16 16"><circle cx="8" cy="8" r="8" fill="#fff"/><path d="M4.5 8 L7 10.5 L11.5 5.5" stroke="#1a9a7c" stroke-width="2" fill="none"/></svg>Practical &amp; Sustainable</li>
  <li><svg width="16" height="16" viewBox="0 0 16 16"><circle cx="8" cy="8" r="8" fill="#fff"/><path d="M4.5 8 L7 10.5 L11.5 5.5" stroke="#1a9a7c" stroke-width="2" fill="none"/></svg>Compassionate &amp; Neuro-Affirming</li>
</ul>

<!-- difference -->
<div class="abs diff-icon"><svg width="60" height="60" viewBox="0 0 60 60" fill="#fff"><rect x="10" y="22" width="40" height="26" rx="4"/><path d="M22 48 L18 56 L30 48 Z"/><rect x="18" y="30" width="24" height="3" fill="#1a9f80"/><rect x="18" y="37" width="18" height="3" fill="#1a9f80"/><circle cx="18" cy="12" r="4"/><circle cx="30" cy="10" r="4"/><circle cx="42" cy="12" r="4"/></svg></div>
<h2 class="abs head diff-title">Because sometimes the smallest change can make the biggest difference</h2>
<p class="abs diff-text">Whether you are looking to better understand yourself, develop new strategies, receive practical support or simply have someone who understands, I'm here for you.</p>
<div class="abs badge" style="left:83px"><div class="shape"><svg width="90" height="90"><rect x="5" y="5" width="80" height="80" rx="10" fill="#e2efeb"/></svg></div><div class="label">Open Meadow Academy</div></div>
<div class="abs badge" style="left:441px"><div class="shape"><svg width="90" height="90"><rect x="5" y="5" width="80" height="80" rx="10" fill="#e2efeb"/></svg></div><div class="label">The Coaching Guild</div></div>
<div class="abs badge" style="left:799px"><div class="shape"><svg width="90" height="90"><rect x="5" y="5" width="80" height="80" rx="10" fill="#e2efeb"/></svg></div><div class="label">Care Pathways Institute</div></div>

<!-- cta -->
<section class="abs cta"></section>
<h2 class="abs head cta-title">Discover your inner strength &amp;<br>cultivate a balanced life</h2>
<div class="abs btn cta-btn">Contact Velbrin</div>
<footer class="abs footer">(C) Copyright | All Rights Reserved</footer>

</body>
</html>
```